Need a fresh corporate identity for an existing Home Shopping Business in Thailand

We are one of the most active TV home shopping companies in Thailand. We need a fresh looking CI for our corporate, the colours of our corporate are Orange and Grey. We want our customers to see us as professional customer service who help them with their purchases.
The logo can be shown as a whole logo or either half logo but not less than half the logo.
Industry/Entity Type
Shopping
Requirements
Must have
- The logo should be shown at least half the logo or full logo.
Should not have
- The logo should not be shown less than half the logo.

```html
<!DOCTYPE html>
<html lang="en">
<head>
<meta charset="utf-8">
<title>HomeHarbor Stationery</title>
<link rel="stylesheet" href="https://fonts.googleapis.com/css2?family=Arimo:wght@400&display=swap">
<style>
  :root {
    --board: #231f20;
    --paper: #ffffff;
    --brand-orange: #e05a16;
    --brand-grey: #8a8a8a;
    --text-grey: #6d6d6d;
    --rule-grey: #a5a5a5;
    --ghost: #f1f1f1;
    --shadow: rgba(0,0,0,0.55);
    --ink-m: #ec008c;
    --ink-c: #00aeef;
    --ink-k: #000000;
    --ink-y: #fff200;
  }
  * { box-sizing: border-box; margin: 0; padding: 0; }
  html, body { width: 1200px; height: 800px; overflow: hidden; background: var(--board); }
  body { position: relative; font-family: "Arimo", Arial, sans-serif; }

  .sheet, .envelope, .flap { position: absolute; background: var(--paper); overflow: hidden; }

  /* Letterhead */
  .sheet { width: 526px; height: 744px; box-shadow: 3px 3px 6px var(--shadow); }
  .sheet--back { left: 33px; top: 36px; }
  .sheet--front { left: 23px; top: 26px; }

  .ghost-mark { position: absolute; border-radius: 50%; background: var(--ghost); }
  .sheet .ghost-mark { width: 420px; height: 420px; left: 282px; top: 110px; }

  .band { position: absolute; left: 0; right: 0; bottom: 0; display: flex; }
  .band__grey { background: var(--brand-grey); }
  .band__orange { background: var(--brand-orange); }
  .sheet .band { height: 18px; }
  .sheet .band__grey { width: 412px; }
  .sheet .band__orange { flex: 1; }

  .address {
    position: absolute; border-left: 1px solid var(--rule-grey);
    padding-left: 5px; font-size: 9px; line-height: 16px; color: var(--text-grey);
  }
  .sheet .address { left: 17px; top: 673px; }
  .address .phone-label { margin-right: 6px; }

  .brand { position: absolute; display: flex; flex-direction: column; align-items: center; color: var(--brand-orange); font-size: 10px; }
  .brand__dot { border-radius: 50%; background: var(--brand-orange); }
  .brand__name { margin-top: 8px; white-space: nowrap; }
  .brand__name sup { font-size: 6px; margin-left: 2px; }
  .sheet .brand { left: 432px; top: 643px; }
  .sheet .brand__dot { width: 56px; height: 56px; }

  /* Envelopes */
  .envelope { box-shadow: 3px 3px 6px var(--shadow); }
  .envelope--front { left: 604px; top: 218px; width: 582px; height: 247px; }
  .envelope--back { left: 578px; top: 36px; width: 584px; height: 248px; }

  .flap {
    left: 0; top: 0; width: 584px; height: 79px;
    border-radius: 0 0 38px 38px;
    border-bottom: 1px solid #d9d9d9;
    box-shadow: 0 3px 4px rgba(0,0,0,0.45);
  }
  .flap .ghost-mark { width: 100px; height: 100px; left: 240px; top: 24px; }

  .window { position: absolute; left: 17px; top: 82px; width: 314px; height: 85px; border: 1px solid #b5b5b5; border-radius: 10px; }
  .envelope--front .address { left: 18px; top: 180px; }
  .envelope--front .band { height: 10px; }
  .envelope--front .band__grey { width: 477px; }
  .envelope--front .band__orange { flex: 1; }
  .envelope--front .brand { left: 503px; top: 172px; font-size: 9px; }
  .envelope--front .brand__dot { width: 46px; height: 46px; }
  .envelope--front .brand__name { margin-top: 6px; }

  /* Process ink swatches */
  .inks { position: absolute; left: 1058px; top: 661px; display: grid; grid-template-columns: 55px 55px; gap: 9px; }
  .ink {
    width: 55px; height: 55px; border-radius: 50%; border: 2px solid #fff;
    display: flex; align-items: center; justify-content: center;
    font-size: 20px; color: #fff;
  }
  .ink--m { background: var(--ink-m); }
  .ink--c { background: var(--ink-c); }
  .ink--k { background: var(--ink-k); }
  .ink--y { background: var(--ink-y); color: #fff; }
</style>
</head>
<body>

  <div class="sheet sheet--back">
    <div class="ghost-mark"></div>
    <div class="band"><div class="band__grey"></div><div class="band__orange"></div></div>
  </div>

  <section class="sheet sheet--front" aria-label="Letterhead">
    <div class="ghost-mark"></div>
    <address class="address">
      58/17 Riverline Trade Tower.<br>
      Bang Rak, Krung Thep, Thailand 10500<br>
      <span class="phone-label">Phone</span>+66 2 410 3926
    </address>
    <div class="brand">
      <div class="brand__dot"></div>
      <div class="brand__name">HomeHarbor<sup>™</sup></div>
    </div>
    <div class="band"><div class="band__grey"></div><div class="band__orange"></div></div>
  </section>

  <section class="envelope envelope--front" aria-label="Envelope front">
    <div class="window"></div>
    <address class="address">
      58/17 Riverline Trade Tower.<br>
      Bang Rak, Krung Thep, Thailand 10500<br>
      <span class="phone-label">Phone</span>+66 2 410 3926
    </address>
    <div class="brand">
      <div class="brand__dot"></div>
      <div class="brand__name">HomeHarbor<sup>™</sup></div>
    </div>
    <div class="band"><div class="band__grey"></div><div class="band__orange"></div></div>
  </section>

  <section class="envelope envelope--back" aria-label="Envelope back">
    <div class="flap"><div class="ghost-mark"></div></div>
  </section>

  <div class="inks" aria-label="Process colours">
    <div class="ink ink--m">M</div>
    <div class="ink ink--c">C</div>
    <div class="ink ink--k">K</div>
    <div class="ink ink--y">Y</div>
  </div>

</body>
</html>
```